New solo practice law firm is looking for an elegant, professional, and interactive web design

I need a web design and developer for a new small law firm in Sacramento, California called Dorian Kessly Law, A Professional Corporation. I am a trial lawyer who represents average people facing difficult litigation disputes, including criminal defense as a former prosecutor and civil litigation as a civil litigator. Criminal defense includes domestic violence, battery, assault, drug possession, theft, DUI, etc. Civil litigation includes business disputes, property disputes, employment disputes, family law disputes, and immigration issues. I would like to see web designs that incorporate my logo and use the logo's navy blue and gold colors. I have uploaded the files of my logo to this brief. Please only use the navy blue and gold version. Overall, I want the design to look firm, professional, and elegant.

I plan on having the following pages on my website: (1) Home, (2) Dorian Kessly, (3) Practice Areas, (4) Insights, (5) Contact. I've hand drawn a preliminary sketch concept of what I envision the home page's layout to look like (attached with a text version). I would like your design to keep a similar layout for the homepage and incorporate my logo's colors within it but I am open to creative layout alternatives/ideas. I would like the other pages to have a similar look and feel as the home page. Some of the areas currently in my sketch do not have the full text. You can insert other text for now and I will provide the winner the full text.

In terms of the pictures on the website, I enjoy images of courthouses, columns (example attached but I cannot use this one), and, if possible, images from Sacramento, CA in my background (headshot attached). A plus would be live images that move and also sections of the webpage moving in the viewers view as they scroll down on the page. Also, it would be great to have my logo act as the tab for the website. I can provide other versions of the logo if needed.

I look forward to seeing your Wordpress designs!

People needing legal representation.

Law

Coded - Design and coding required

5+ page

Serif

• Incorporate my logo and my logo's colors.
• Live pictures and images appearing as viewers scroll on page.

```html
<!DOCTYPE html>
<html lang="en">
<head>
<meta charset="utf-8">
<title>Family Law — Dorian Kessly Law</title>
<link rel="stylesheet" href="https://fonts.googleapis.com/css2?family=Cinzel:wght@400;600&family=Montserrat:wght@400;500;600;700&display=swap">
<style>
:root{
  --navy:#0f1a33;
  --navy-deep:#0a1226;
  --gold:#c9a45c;
  --gold-soft:#d8bb7e;
  --ink:#1d2230;
  --muted:#6b6f7a;
  --white:#ffffff;
  --line:rgba(201,164,92,.35);
}
*{margin:0;padding:0;box-sizing:border-box}
html,body{width:1200px;height:2172px;overflow:hidden;background:var(--white)}
body{position:relative;font-family:"Montserrat",Arial,sans-serif;color:var(--ink)}

/* hero */
.hero{position:absolute;left:0;top:0;width:1200px;height:500px;
  background:linear-gradient(180deg,#0c1530 0%,#1a2747 55%,#33405e 100%)}
.hero-cut{position:absolute;left:0;top:400px;width:1200px;height:100px}
.lang{position:absolute;right:40px;top:8px;font-size:13px;color:var(--white)}
.brand{position:absolute;left:0;right:0;top:58px;text-align:center;color:var(--gold)}
.brand .name{font-family:"Cinzel",Georgia,serif;font-size:30px;font-weight:600;letter-spacing:6px;display:flex;align-items:center;justify-content:center;gap:16px}
.brand .name i{display:block;width:34px;height:34px;background:var(--gold)}
.brand .sub{font-family:"Cinzel",Georgia,serif;font-size:12px;font-weight:600;letter-spacing:5px;margin-top:6px}
.cta{position:absolute;right:60px;top:64px;width:150px;height:44px;border:1px solid var(--gold);
  color:var(--white);font-size:9px;letter-spacing:1px;padding:9px 12px;line-height:13px}
.cta b{display:block;font-weight:700}
.nav{position:absolute;left:0;right:0;top:152px;display:flex;justify-content:center;gap:30px;font-size:14px;font-weight:600;color:var(--white);letter-spacing:.5px}
.nav span{padding:6px 8px}
.nav .active{border:1px solid var(--gold);color:var(--gold)}
.hero-title{position:absolute;left:0;right:0;top:245px;text-align:center;font-family:"Cinzel",Georgia,serif;font-size:78px;font-weight:400;color:var(--gold-soft);letter-spacing:3px}

/* intro */
.intro-photo{position:absolute;left:100px;top:600px;width:340px;height:260px;
  background:linear-gradient(180deg,#f2c98a 0%,#e8a861 45%,#5d5f6b 75%,#2f3444 100%)}
.intro-dots{position:absolute;left:60px;top:800px;width:100px;height:100px}
.intro-text{position:absolute;left:538px;top:628px;width:560px}
.intro-text h2{font-size:30px;font-weight:700;color:var(--ink);letter-spacing:1px}
.intro-text p{margin-top:14px;font-size:14.5px;line-height:25px;color:var(--muted)}

/* cases */
.cases-title{position:absolute;left:0;right:0;top:990px;text-align:center;font-size:42px;font-weight:700;letter-spacing:1px;color:var(--ink)}
.case{position:absolute;width:290px}
.case svg{display:block;width:54px;height:54px}
.case h3{margin-top:12px;font-size:14px;font-weight:700;color:var(--ink)}
.case p{margin-top:6px;font-size:12.5px;line-height:19px;color:var(--muted)}

/* footer */
.footer-cut{position:absolute;left:0;top:1500px;width:1200px;height:110px}
.footer{position:absolute;left:0;top:1608px;width:1200px;height:564px;background:var(--navy)}
.f-brand{position:absolute;left:90px;top:230px;color:var(--gold)}
.f-brand .name{font-family:"Cinzel",Georgia,serif;font-size:22px;font-weight:600;letter-spacing:4px;display:flex;align-items:center;gap:12px}
.f-brand .name i{display:block;width:26px;height:26px;background:var(--gold)}
.f-brand .sub{font-family:"Cinzel",Georgia,serif;font-size:10px;font-weight:600;letter-spacing:3px;margin-top:5px;padding-left:38px}
.f-col h4{font-size:18px;font-weight:500;letter-spacing:1px;color:var(--gold);margin-bottom:16px}
.f-contact{position:absolute;left:580px;top:170px;width:300px}
.f-row{display:flex;gap:12px;font-size:12.5px;line-height:18px;color:var(--white);margin-bottom:12px}
.f-row svg{flex:0 0 16px;width:16px;height:16px;margin-top:1px}
.social{display:flex;gap:10px;margin-top:6px}
.social i{display:block;width:24px;height:24px;border-radius:50%;background:var(--gold)}
.f-links{position:absolute;left:905px;top:170px}
.f-links li{list-style:none;font-size:13px;color:var(--white);margin-bottom:9px;padding-left:14px;position:relative}
.f-links li::before{content:"";position:absolute;left:0;top:6px;width:5px;height:5px;background:var(--gold)}
.f-rule{position:absolute;left:90px;right:90px;top:395px;height:1px;background:var(--line)}
.f-note{position:absolute;left:250px;right:250px;top:418px;text-align:center;font-size:11px;line-height:17px;color:#b9bfcc}
.f-copy{position:absolute;left:0;right:0;top:505px;text-align:center;font-size:12px;font-weight:600;color:var(--white)}
.to-top{position:absolute;right:40px;top:482px;width:38px;height:38px;background:var(--gold)}
</style>
</head>
<body>

<header class="hero" role="img" aria-label="Night skyline of Sacramento under a deep navy sky">
  <div class="lang">English ▾</div>
  <div class="brand">
    <div class="name"><i></i>DORIAN KESSLY LAW</div>
    <div class="sub">A PROFESSIONAL CORPORATION</div>
  </div>
  <div class="cta">SCHEDULE A <b>FREE CONSULTATION</b></div>
  <nav class="nav">
    <span>HOME</span><span>DORIAN KESSLY</span><span class="active">PRACTICE AREAS</span><span>INSIGHTS</span><span>CONTACT</span>
  </nav>
  <h1 class="hero-title">FAMILY LAW</h1>
</header>
<svg class="hero-cut" viewBox="0 0 1200 100" preserveAspectRatio="none"><polygon points="0,100 0,70 1200,0 1200,100" fill="#ffffff"/></svg>

<section>
  <div class="intro-photo" role="img" aria-label="Family holding hands on a beach at sunset"></div>
  <svg class="intro-dots" viewBox="0 0 100 100">
    <g fill="#c9a45c">
      <circle cx="10" cy="10" r="2"/><circle cx="30" cy="10" r="2"/><circle cx="50" cy="10" r="2"/><circle cx="70" cy="10" r="2"/>
      <circle cx="10" cy="30" r="2"/><circle cx="30" cy="30" r="2"/><circle cx="50" cy="30" r="2"/><circle cx="70" cy="30" r="2"/>
      <circle cx="10" cy="50" r="2"/><circle cx="30" cy="50" r="2"/><circle cx="50" cy="50" r="2"/><circle cx="70" cy="50" r="2"/>
      <circle cx="10" cy="70" r="2"/><circle cx="30" cy="70" r="2"/><circle cx="50" cy="70" r="2"/><circle cx="70" cy="70" r="2"/>
    </g>
  </svg>
  <div class="intro-text">
    <h2>CHOOSE THE RIGHT LAWYER</h2>
    <p>Finding the right lawyer is crucial when your parental rights, marital rights, and personal finances are on the line. The right lawyer listens to your needs and focuses their efforts on what matters to you. You need a lawyer by your side that not only understands how to file the proper pleadings, petitions, motions, and discovery, but also a lawyer who is at the same time thinking about the big picture of collecting all the needed information to tell the right story to the court, with the right facts, and using the right law. At Dorian Kessly Law, you will receive the legal representation you need and deserve.</p>
  </div>
</section>

<section>
  <h2 class="cases-title">CASES WE HANDLE</h2>

  <div class="case" style="left:140px;top:1080px">
    <svg viewBox="0 0 54 54" fill="none" stroke="#c9a45c" stroke-width="2"><circle cx="18" cy="30" r="11"/><circle cx="34" cy="30" r="11"/><path d="M22 10l4 5 4-5"/></svg>
    <h3>DIVORCE AND SEPARATION</h3>
    <p>Up to 95% of a merchant's budget is spent on commissions charge by a number of brokers.</p>
  </div>
  <div class="case" style="left:470px;top:1080px">
    <svg viewBox="0 0 54 54" fill="none" stroke="#c9a45c" stroke-width="2"><circle cx="18" cy="14" r="5"/><circle cx="36" cy="20" r="4"/><path d="M10 44V28a8 8 0 0116 0v16M30 44V32a6 6 0 0112 0v12"/></svg>
    <h3>CHILD CUSTODY AND VISITATION</h3>
    <p>Up to 95% of a merchant's budget is spent on commissions charge by a number of brokers.</p>
  </div>
  <div class="case" style="left:800px;top:1080px">
    <svg viewBox="0 0 54 54" fill="none" stroke="#c9a45c" stroke-width="2"><circle cx="27" cy="14" r="6"/><path d="M8 38c6-6 12-6 19-2h9a3 3 0 010 6H24M8 46h26l12-8"/></svg>
    <h3>CHILD SUPPORT</h3>
    <p>Up to 95% of a merchant's budget is spent on commissions charge by a number of brokers.</p>
  </div>
  <div class="case" style="left:140px;top:1260px">
    <svg viewBox="0 0 54 54" fill="none" stroke="#c9a45c" stroke-width="2"><circle cx="20" cy="16" r="5"/><circle cx="34" cy="16" r="5"/><path d="M10 44V32a10 10 0 0120 0M24 32a10 10 0 0120 0v12"/></svg>
    <h3>SPOUSAL SUPPORT</h3>
    <p>Up to 95% of a merchant's budget is spent on commissions charge by a number of brokers.</p>
  </div>
  <div class="case" style="left:470px;top:1260px">
    <svg viewBox="0 0 54 54" fill="none" stroke="#c9a45c" stroke-width="2"><path d="M27 6l16 6v12c0 10-7 17-16 22-9-5-16-12-16-22V12z"/><path d="M21 26l5 5 8-9"/></svg>
    <h3>DOMESTIC VIOLENCE RES...</h3>
    <p>Up to 95% of a merchant's budget is spent on commissions charge by a number of brokers.</p>
  </div>
  <div class="case" style="left:800px;top:1260px">
    <svg viewBox="0 0 54 54" fill="none" stroke="#c9a45c" stroke-width="2"><path d="M14 8h20l8 8v30H14z"/><path d="M20 24h16M20 31h16M20 38h10"/></svg>
    <h3>UNCONTESTED DIVORCE</h3>
    <p>Up to 95% of a merchant's budget is spent on commissions charge by a number of brokers.</p>
  </div>
</section>

<svg class="footer-cut" viewBox="0 0 1200 110" preserveAspectRatio="none"><polygon points="0,110 1200,110 1200,0 0,90" fill="#0f1a33"/></svg>
<footer class="footer">
  <div class="f-brand">
    <div class="name"><i></i>DORIAN KESSLY LAW</div>
    <div class="sub">A PROFESSIONAL CORPORATION</div>
  </div>

  <div class="f-col f-contact">
    <h4>CONTACT INFO</h4>
    <div class="f-row">
      <svg viewBox="0 0 16 16" fill="none" stroke="#c9a45c" stroke-width="1.5"><path d="M8 15s5-5 5-9a5 5 0 00-10 0c0 4 5 9 5 9z"/><circle cx="8" cy="6" r="1.8"/></svg>
      <span>1420 Harbor Ridge Blvd<br>Suite 210<br>Sacramento, CA 95814</span>
    </div>
    <div class="f-row">
      <svg viewBox="0 0 16 16" fill="none" stroke="#c9a45c" stroke-width="1.5"><path d="M3 2h3l1.5 3.5-2 1.2a8 8 0 003.8 3.8l1.2-2L14 10v3a1 1 0 01-1 1A11 11 0 012 3a1 1 0 011-1z"/></svg>
      <span>T: (916) 555-0148</span>
    </div>
    <div class="f-row">
      <svg viewBox="0 0 16 16" fill="none" stroke="#c9a45c" stroke-width="1.5"><rect x="1.5" y="3.5" width="13" height="9"/><path d="M1.5 3.5L8 9l6.5-5.5"/></svg>
      <span>info@doriankesslylaw.com</span>
    </div>
    <div class="social"><i></i><i></i><i></i><i></i></div>
  </div>

  <div class="f-col f-links">
    <h4>QUICK LINKS</h4>
    <ul>
      <li>Home</li><li>Dorian Kessly</li><li>Practice Areas</li><li>Insights</li><li>Contact</li><li>Privacy Policy</li>
    </ul>
  </div>

  <div class="f-rule"></div>
  <p class="f-note">The information on this website is for general information purposes only. Nothing on this site should be taken as legal advice for any individual case or situation. Viewing it does not create an attorney–client relationship.</p>
  <div class="f-copy">© Copyright 2021 All Rights Reserved</div>
  <svg class="to-top" viewBox="0 0 38 38"><rect width="38" height="38" fill="#c9a45c"/><path d="M13 22l6-6 6 6" fill="none" stroke="#0f1a33" stroke-width="2"/></svg>
</footer>

</body>
</html>
```